Velorix Flyer

PROJECT: Digital Flyer for VeloRix

Format
1920 × 1080 px (landscape, optimized for presentations and email)
Deliverables
• PDF
• PNG

About VeloRix
VeloRix is a Dutch B2B software company providing a unified CRM and customer journey platform. We help businesses manage the entire customer lifecycle — from first contact to loyal customer — by centralizing all touchpoints in one system.
What sets us apart:
Extreme ease of use. The system is self-guiding, shows only what's relevant per employee, and requires virtually no training. All channels (email, phone, chat, in-store) come together in one place with automatic task distribution. Built-in AI functions as a smart digital colleague that continuously learns.
Target audience:
Directors and sales managers at B2B companies with multiple customer contact channels.

Goal:
We want to create a flyer that sets us apart from other CRM platform providers. Our aim is to achieve this through simplicity and a professional appearance. The design should reflect our core value: ease of use. The recipient should feel compelled to engage with us — not overwhelmed by information, but intrigued by clarity. Less is more.

Required Text Elements
Headline:
"CRM that adapts to how you work"
Subline:
"Discover how VeloRix simplifies your sales process"
Call-to-action:
"See it in action — book a call"
Contact details:
• hello@velorix.nl
• 023-5718469
• velorix.com

Required Visual Elements
• VeloRix logo (attached)

Design Style
• Modern / Minimalist
• Professional / Business
• Tech / Futuristic
• Clean with plenty of whitespace

Tone of voice:
Clear, positive and customer-focused. Practical and accessible business style aimed at communicating concrete value for users.

Design inspiration — please review these websites:
• orbantal.com
• ravelo.app
• quendo.com
• tirameld.com
• gonwisp.com
What We DON'T Want
• Bold / In-your-face
• Dense / Compact
• Trendy / Experimental
• Childlike / Cheerful
• Playful / Cartoonish
• Busy / Chaotic
Colors
Use the color palette from velorix.com (blues, whites, clean professional tones).
[Exact hex codes used for element on the website:
#344054;
#1a1b1f;
#0254ac
#002249;
#e5edf7;
background-color: #fff; ]
Competitors (for context only — do NOT copy)
• brinvolt.nl
• kelmarin.com
• dortavecrm.com
• wexalunda.com
Budget
$150
Deadline
January 26, 2026

```html
<!DOCTYPE html>
<html lang="en">
<head>
<meta charset="utf-8">
<title>VeloRix Flyer</title>
<link rel="stylesheet" href="https://fonts.googleapis.com/css2?family=Poppins:wght@400;500;700;800&display=swap">
<style>
  :root {
    --page-bg: #dedede;
    --navy: #0f2153;
    --sky: #1a9ad9;
    --ink: #1e2a44;
    --flyer-light: #f7f7f7;
    --flyer-mid: #e6e6e6;
    --white: #ffffff;
  }
  * { margin: 0; padding: 0; box-sizing: border-box; }
  html, body {
    width: 1200px; height: 960px; overflow: hidden;
    background: var(--page-bg);
    font-family: "Poppins", sans-serif;
  }
  .flyer {
    position: absolute; left: 56px; top: 174px;
    width: 1088px; height: 612px; overflow: hidden;
    background: linear-gradient(120deg, var(--flyer-mid) 0%, var(--flyer-light) 35%, var(--white) 55%, var(--flyer-mid) 100%);
  }
  .flyer-lines { position: absolute; inset: 0; }
  .brand {
    position: absolute; left: 107px; top: 88px;
    display: flex; align-items: center; gap: 16px;
  }
  .brand-dot { width: 56px; height: 56px; border-radius: 50%; background: var(--navy); }
  .brand-name { font-weight: 700; font-size: 52px; color: var(--navy); letter-spacing: -0.5px; }
  .headline {
    position: absolute; left: 105px; top: 220px;
    font-weight: 800; font-size: 71px; line-height: 75px;
    color: var(--navy); letter-spacing: -0.5px;
  }
  .headline .accent { color: var(--sky); }
  .subline {
    position: absolute; left: 107px; top: 392px;
    font-weight: 400; font-size: 25.5px; color: var(--sky);
  }
  .cta {
    position: absolute; left: 107px; top: 452px;
    width: 475px; height: 39px; border-radius: 20px;
    background: var(--navy); color: var(--white);
    display: flex; align-items: center; justify-content: center;
    font-weight: 700; font-size: 23px; letter-spacing: -0.3px;
    box-shadow: 0 12px 14px -8px rgba(0,0,0,0.35);
  }
  .contact {
    position: absolute; left: 105px; top: 554px;
    display: flex; align-items: center; gap: 8px;
    font-weight: 400; font-size: 23px; color: var(--ink);
  }
  .contact-item { display: flex; align-items: center; gap: 7px; margin-right: 2px; }
  .contact-icon { width: 23px; height: 23px; flex: none; }
</style>
</head>
<body>
  <section class="flyer">
    <svg class="flyer-lines" viewBox="0 0 1088 612" preserveAspectRatio="none" aria-hidden="true">
      <polygon points="775,167 1088,0 1088,612 880,612" fill="#d9d9d9" opacity="0.35"/>
      <polygon points="0,440 200,380 340,612 0,612" fill="#ececec" opacity="0.6"/>
      <polygon points="380,0 560,0 620,260" fill="#ffffff" opacity="0.5"/>
      <g stroke="#ffffff" stroke-width="2" fill="none">
        <line x1="0" y1="78" x2="340" y2="350"/>
        <line x1="0" y1="350" x2="290" y2="550"/>
        <line x1="495" y1="0" x2="1088" y2="588"/>
        <line x1="742" y1="0" x2="1022" y2="612"/>
        <line x1="510" y1="10" x2="1088" y2="520"/>
        <line x1="775" y1="167" x2="1088" y2="175"/>
        <line x1="560" y1="210" x2="775" y2="167"/>
      </g>
    </svg>

    <div class="brand">
      <span class="brand-dot"></span>
      <span class="brand-name">VeloRix</span>
    </div>

    <h1 class="headline"><span class="accent">CRM</span> that adapts to<br>how you work</h1>

    <p class="subline">Discover how VeloRix simplifies your sales process</p>

    <div class="cta">SEE IT IN ACTION — BOOK A CALL</div>

    <div class="contact">
      <span class="contact-item">
        <svg class="contact-icon" viewBox="0 0 24 24" aria-hidden="true"><rect x="1" y="5" width="22" height="14" fill="#1a9ad9"/><path d="M1 5 L12 13 L23 5 M1 19 L9 11 M23 19 L15 11" stroke="#fff" stroke-width="1.4" fill="none"/></svg>
        hello@velorix.nl
      </span>
      <span class="contact-item">
        <svg class="contact-icon" viewBox="0 0 24 24" aria-hidden="true"><circle cx="12" cy="12" r="11.5" fill="#1a9ad9"/><path d="M8 6 l2 0 l1 3 l-1.5 1.2 a8 8 0 0 0 4.3 4.3 l1.2-1.5 l3 1 l0 2 a2 2 0 0 1-2 1.5 a11 11 0 0 1-10-10 a2 2 0 0 1 2-1.5z" fill="#fff"/></svg>
        023-5718469
      </span>
      <span class="contact-item">
        <svg class="contact-icon" viewBox="0 0 24 24" aria-hidden="true"><circle cx="12" cy="12" r="11" fill="#1a9ad9"/><g stroke="#fff" stroke-width="1.2" fill="none"><ellipse cx="12" cy="12" rx="4.5" ry="11"/><line x1="12" y1="1" x2="12" y2="23"/><line x1="1" y1="12" x2="23" y2="12"/><path d="M3 6.5 H21 M3 17.5 H21"/></g></svg>
        velorix.com
      </span>
    </div>
  </section>
</body>
</html>
```